Brightwell Letterhead

We would like a letterhead for our company. I have uploaded our logo.

Brightwell Peak Consulting
1450 W Corvin Rd Ste 310
Hollis Springs, TX 75840
844-555-0172

```html
<!DOCTYPE html>
<html lang="en">
<head>
<meta charset="utf-8">
<title>Brightwell Peak Consulting Letterhead</title>
<link rel="stylesheet" href="https://fonts.googleapis.com/css2?family=Source+Sans+3:wght@400;600&family=Open+Sans:wght@400;600&family=Allura&display=swap">
<style>
  :root {
    --backdrop: #e4e4e4;
    --paper: #ffffff;
    --teal: #0a5c6b;
    --mint: #6cc497;
    --ink: #4a4a4a;
    --signature: #1d4f6b;
  }
  html, body {
    margin: 0;
    padding: 0;
    width: 1200px;
    height: 1141px;
    overflow: hidden;
    background: var(--backdrop);
  }
  .letterhead {
    position: absolute;
    left: 210px;
    top: 23px;
    width: 780px;
    height: 1094px;
    background: var(--paper);
    box-shadow: 0 2px 8px rgba(0,0,0,0.18);
    font-family: "Source Sans 3", sans-serif;
    color: var(--ink);
    overflow: hidden;
  }
  .brand {
    position: absolute;
    top: 64px;
    left: 0;
    width: 100%;
    display: flex;
    justify-content: center;
    align-items: center;
    gap: 10px;
  }
  .brand-dot {
    width: 26px;
    height: 26px;
    border-radius: 50%;
    background: var(--teal);
  }
  .brand-name {
    font-family: "Source Sans 3", sans-serif;
    font-weight: 600;
    font-size: 24px;
    line-height: 28px;
    color: var(--teal);
  }
  .recipient {
    position: absolute;
    left: 58px;
    top: 280px;
  }
  .recipient-name {
    font-size: 16px;
    margin: 0 0 3px;
    text-transform: uppercase;
    font-weight: 400;
  }
  .recipient-line {
    font-size: 12px;
    line-height: 19px;
    margin: 0;
  }
  .letter-body {
    position: absolute;
    left: 58px;
    top: 378px;
    width: 663px;
    font-size: 12px;
    line-height: 19.2px;
    text-align: justify;
  }
  .letter-body p {
    margin: 0 0 16px;
  }
  .closing {
    position: absolute;
    left: 58px;
    top: 680px;
    font-size: 12.5px;
    margin: 0;
  }
  .signature {
    position: absolute;
    left: 56px;
    top: 700px;
    font-family: "Allura", cursive;
    font-size: 34px;
    color: var(--signature);
    margin: 0;
  }
  .footer-accent {
    position: absolute;
    left: 0;
    bottom: 62px;
    width: 100%;
    height: 4px;
    background: var(--mint);
  }
  .footer-info {
    position: absolute;
    left: 0;
    bottom: 0;
    width: 100%;
    height: 58px;
    background: var(--teal);
    font-family: "Open Sans", sans-serif;
    color: #ffffff;
    text-align: center;
  }
  .footer-address {
    position: absolute;
    top: 10px;
    width: 100%;
    font-size: 13px;
    margin: 0;
  }
  .footer-address strong {
    font-weight: 600;
  }
  .footer-phone {
    position: absolute;
    top: 30px;
    left: 158px;
    width: 464px;
    display: flex;
    align-items: center;
    gap: 8px;
    font-size: 13px;
  }
  .footer-rule {
    flex: 1;
    height: 1px;
    background: var(--mint);
  }
  .footer-phone svg {
    width: 12px;
    height: 12px;
  }
</style>
</head>
<body>
  <main class="letterhead">
    <header class="brand">
      <span class="brand-dot"></span>
      <span class="brand-name">Brightwell Peak Consulting</span>
    </header>

    <section class="recipient">
      <h2 class="recipient-name">Darren Holloway</h2>
      <p class="recipient-line">President / CEO</p>
      <p class="recipient-line">City/State, Zip Code</p>
    </section>

    <section class="letter-body">
      <p>Lorem Ipsum is simply dummy text of the printing and typesetting industry. Lorem Ipsum has been the industry's standard dummy text ever since the 1500s, when an unknown printer took a galley of type and scrambled it to make a type specimen book. It has survived not only five centuries, but also the leap into electronic typesetting, remaining essentially unchanged. It was popularised in the 1960s with the release of Vellum Press sheets containing Lorem Ipsum passages, and more recently with desktop publishing software like Quillset Layout including versions of Lorem Ipsum.</p>
      <p>It is a long established fact that a reader will be distracted by the readable content of a page when looking at its layout. The point of using Lorem Ipsum is that it has a more-or-less normal distribution of letters, as opposed to using 'Content here, content here', making it look like readable English. Many desktop publishing packages and web page editors now use Lorem Ipsum as their default model text, and a searchaccident, sometimes on purpose (injected humour and the like).</p>
      <p>There are many variations of passages of Lorem Ipsum available, but the majority have suffered alteration in some form, by injected humour, or randomised words which don't look even slightly believable. If you are going to use a passage of Lorem Ipsum, you need to be sure there isn't anything embarrassing hidden in the middle of text.</p>
    </section>

    <p class="closing">Sincerely,</p>
    <p class="signature">Lena Marsh</p>

    <div class="footer-accent"></div>
    <footer class="footer-info">
      <p class="footer-address"><strong>Brightwell Peak Consulting -</strong> 1450 W Corvin Rd Ste 310, Hollis Springs, TX 75840</p>
      <div class="footer-phone">
        <span class="footer-rule"></span>
        <svg viewBox="0 0 24 24" aria-hidden="true"><path d="M6.6 10.8a15 15 0 0 0 6.6 6.6l2.2-2.2a1 1 0 0 1 1-.25 11.4 11.4 0 0 0 3.6.57 1 1 0 0 1 1 1V20a1 1 0 0 1-1 1A17 17 0 0 1 3 4a1 1 0 0 1 1-1h3.5a1 1 0 0 1 1 1c0 1.25.2 2.45.57 3.57a1 1 0 0 1-.25 1z" fill="#6cc497"/></svg>
        <span>844-555-0172</span>
        <span class="footer-rule"></span>
      </div>
    </footer>
  </main>
</body>
</html>
```